Business Cards for a law firm

Business cards for our law firm. Use our silhoette logo and OAK HARBOR - check our website (www.oakharbor-legal.com)

Contact Information for Business Card

our silhouette logo, OAK HARBOR, 800-555-0147, Dorian Kestrup, dorian@oakharbor-legal.com

Requirements
Must have
• our silhouette logo, OAK HARBOR, 800-555-0147, Dorian Kestrup, dorian@oakharbor-legal.com

```html
<!DOCTYPE html>
<html lang="en">
<head>
<meta charset="utf-8">
<title>Oak Harbor — Business Card</title>
<link rel="stylesheet" href="https://fonts.googleapis.com/css2?family=Montserrat:wght@500;600;700&display=swap">
<style>
  :root {
    --ink: #1c3a8e;
    --card: #ffffff;
    --backdrop: #e9e6e1;
    --edge: #d9d6d0;
  }
  html, body {
    margin: 0;
    padding: 0;
    width: 1200px;
    height: 1111px;
    overflow: hidden;
    background: var(--backdrop);
  }
  .canvas {
    position: relative;
    width: 1200px;
    height: 1111px;
  }
  .card {
    position: absolute;
    left: 150px;
    top: 290px;
    width: 900px;
    height: 530px;
    background: var(--card);
    border-radius: 26px;
    box-shadow: 0 2px 0 var(--edge), 0 18px 40px rgba(0,0,0,0.10);
    font-family: "Montserrat", sans-serif;
    color: var(--ink);
  }
  .card__tab {
    position: absolute;
    left: -40px;
    top: 40px;
    width: 120px;
    height: 170px;
    background: var(--card);
    border-radius: 30px;
  }
  .brand {
    position: absolute;
    left: -10px;
    top: 62px;
    display: flex;
    align-items: center;
    gap: 28px;
  }
  .brand__mark {
    width: 96px;
    height: 96px;
    border-radius: 50%;
    background: var(--ink);
    flex: none;
  }
  .brand__name {
    margin: 0;
    font-weight: 700;
    font-size: 64px;
    letter-spacing: 3px;
    line-height: 1;
    white-space: nowrap;
  }
  .person {
    position: absolute;
    left: 120px;
    top: 230px;
  }
  .person__name {
    margin: 0 0 18px;
    font-weight: 700;
    font-size: 26px;
  }
  .person__role {
    margin: 0;
    font-weight: 600;
    font-size: 25px;
  }
  .contact {
    position: absolute;
    left: 120px;
    right: 40px;
    bottom: 70px;
    display: flex;
    gap: 70px;
    font-weight: 500;
    font-size: 25px;
  }
  .contact__item {
    display: flex;
    align-items: center;
    gap: 16px;
    white-space: nowrap;
  }
  .contact__icon {
    width: 26px;
    height: 26px;
    fill: var(--ink);
    flex: none;
  }
</style>
</head>
<body>
<main class="canvas">
  <article class="card">
    <div class="card__tab"></div>
    <header class="brand">
      <span class="brand__mark" aria-hidden="true"></span>
      <h1 class="brand__name">OAK HARBOR</h1>
    </header>
    <section class="person">
      <p class="person__name">Dorian Kestrup</p>
      <p class="person__role">Attorney | Reserve Dep. Sheriff</p>
    </section>
    <footer class="contact">
      <span class="contact__item">
        <svg class="contact__icon" viewBox="0 0 24 24" aria-hidden="true">
          <path d="M6.6 10.8c1.4 2.8 3.8 5.1 6.6 6.6l2.2-2.2c.3-.3.7-.4 1-.2 1.1.4 2.3.6 3.6.6.6 0 1 .4 1 1V20c0 .6-.4 1-1 1C10.6 21 3 13.4 3 4c0-.6.4-1 1-1h3.5c.6 0 1 .4 1 1 0 1.3.2 2.5.6 3.6.1.3 0 .7-.2 1L6.6 10.8z"/>
        </svg>
        800-555-0147
      </span>
      <span class="contact__item">
        <svg class="contact__icon" viewBox="0 0 24 24" aria-hidden="true">
          <path d="M12 2a10 10 0 1 0 0 20 10 10 0 0 0 0-20zm6.9 6h-2.9a15.7 15.7 0 0 0-1.4-3.6A8 8 0 0 1 18.9 8zM12 4c.8 1.2 1.5 2.5 1.9 4h-3.8c.4-1.4 1.1-2.8 1.9-4zM4.3 14a8 8 0 0 1 0-4h3.4a16.5 16.5 0 0 0 0 4H4.3zm.8 2h2.9c.3 1.3.8 2.5 1.4 3.6A8 8 0 0 1 5.1 16zM8 8H5.1a8 8 0 0 1 4.3-3.6C8.8 5.5 8.3 6.7 8 8zm4 12c-.8-1.2-1.5-2.5-1.9-4h3.8c-.4 1.4-1.1 2.8-1.9 4zm2.3-6H9.7a14.7 14.7 0 0 1 0-4h4.6a14.7 14.7 0 0 1 0 4zm.3 5.6c.6-1.1 1.1-2.3 1.4-3.6h2.9a8 8 0 0 1-4.3 3.6zm1.7-5.6a16.5 16.5 0 0 0 0-4h3.4a8 8 0 0 1 0 4h-3.4z"/>
        </svg>
        dorian@oakharbor-legal.com
      </span>
    </footer>
  </article>
</main>
</body>
</html>
```